Saltbush Creek Plumbing Business card & letter head design

We need a new business card and letter head for our plumbing company called saltbush creek plumbing. attached is the companys logo. We provide domestic and commercial plumbing services in regional western Australia. We are after Something simple yet nice to look at and something that fits within the trade industry.

Target Market(s)

trade/building industry

Contact Information for Business Card

Harlan Mossby
Manager
0481 362 740
enquiries@scplumbingco.net.au
ABN: 47 815 203 966
PCL: 4187

Domestic & Commercial Plumbing
Tip Truck & Excavator hire

Colors

Designer to choose colors to be used in the design.

```html
<!DOCTYPE html>
<html lang="en">
<head>
<meta charset="utf-8">
<title>Saltbush Creek Plumbing – Stationery</title>
<link rel="stylesheet" href="https://fonts.googleapis.com/css2?family=Arimo:ital,wght@0,400;0,700;1,400&display=swap">
<style>
  :root {
    --brand-blue: #0b4fa3;
    --brand-navy: #0a3a8a;
    --ink: #3c3f44;
    --rule: #9ea3aa;
    --paper: #ffffff;
    --band-pale: #e8ebf0;
    --stage: #2a3031;
  }
  * { box-sizing: border-box; margin: 0; padding: 0; }
  html, body { width: 1200px; height: 575px; overflow: hidden; }
  body {
    background: var(--stage);
    font-family: "Arimo", Arial, sans-serif;
    color: var(--ink);
    position: relative;
  }
  .sheet {
    position: absolute;
    background: var(--paper);
    box-shadow: 0 6px 18px rgba(0,0,0,.45);
    overflow: hidden;
  }
  .wordmark {
    font-weight: 700;
    color: var(--brand-blue);
    text-transform: uppercase;
    line-height: 1.1;
    letter-spacing: .02em;
  }

  /* Business card — front */
  .card-front { left: 40px; top: 62px; width: 320px; height: 183px; background: var(--brand-blue); }
  .card-front .pattern-band {
    position: absolute; left: 0; top: 62px; width: 100%; height: 64px;
    background: var(--band-pale);
  }
  .card-front .wordmark {
    position: absolute; left: 0; right: 0; top: 78px; text-align: center;
    font-size: 18px;
  }

  /* Business card — back */
  .card-back { left: 40px; top: 290px; width: 320px; height: 183px; }
  .card-back .divider { position: absolute; left: 0; right: 0; top: 62px; border-top: 1px solid var(--rule); }
  .card-back .accent-bar { position: absolute; right: 0; top: 10px; width: 6px; height: 40px; background: var(--brand-blue); }
  .card-back .contact-person { position: absolute; right: 16px; top: 12px; text-align: right; }
  .contact-person .name { font-size: 12px; font-weight: 700; color: var(--brand-blue); }
  .contact-person .role { font-size: 8px; }
  .contact-person .phone { font-size: 11px; font-weight: 700; color: var(--ink); }
  .card-back .wordmark { position: absolute; left: 18px; top: 28px; font-size: 13px; }
  .card-back .services { position: absolute; left: 18px; top: 76px; font-size: 12px; font-weight: 700; line-height: 1.3; }
  .services .primary { color: var(--brand-blue); }
  .services .secondary { color: var(--ink); }
  .services em { font-weight: 700; }
  .card-back .details { position: absolute; left: 18px; top: 120px; font-size: 10px; line-height: 1.45; }

  /* Letterhead */
  .letterhead { left: 404px; top: 22px; width: 384px; height: 531px; }
  .letterhead .wordmark { position: absolute; left: 0; right: 0; top: 22px; text-align: center; font-size: 13px; }
  .letterhead .tagline {
    position: absolute; left: 0; right: 0; bottom: 26px; text-align: center;
    font-size: 8px; color: var(--brand-blue);
  }
  .tagline .sep { color: var(--rule); }
  .letterhead .footer-bar {
    position: absolute; left: 0; right: 0; bottom: 0; height: 20px;
    background: var(--brand-blue); color: #fff; font-size: 6px;
    display: flex; align-items: center; justify-content: space-between; padding: 0 8px;
  }
  .footer-bar .contact { display: flex; align-items: center; gap: 4px; }
  .icon { width: 7px; height: 7px; display: inline-block; vertical-align: middle; }

  /* Envelope */
  .envelope-front { left: 740px; top: 107px; width: 414px; height: 170px; }
  .envelope-front .wordmark { position: absolute; left: 9px; top: 15px; font-size: 7px; }
  .envelope-front .top-rule { position: absolute; left: 0; right: 0; top: 36px; border-top: 1px solid var(--rule); }
  .envelope-front .return-block {
    position: absolute; left: 0; top: 133px; padding-left: 9px;
    border-left: 3px solid var(--brand-navy); font-size: 4px; line-height: 1.35;
  }
  .return-block .services { font-weight: 700; color: var(--brand-blue); font-size: 4.4px; }
  .return-block .services em { font-weight: 400; }
  .return-block .rule { border-top: 1px solid var(--rule); width: 86px; margin: 2px 0; }
  .envelope-back { left: 741px; top: 287px; width: 414px; height: 170px; }
  .envelope-back svg { position: absolute; left: 0; top: 0; }
</style>
</head>
<body>

  <section class="sheet card-front" aria-label="Business card front">
    <div class="pattern-band" role="img" aria-label="Repeating pale brand-name text pattern"></div>
    <div class="wordmark">Saltbush Creek Plumbing</div>
  </section>

  <section class="sheet card-back" aria-label="Business card back">
    <div class="accent-bar"></div>
    <div class="contact-person">
      <div class="name">Harlan Mossby</div>
      <div class="role">Manager</div>
      <div class="phone">0481 362 740</div>
    </div>
    <div class="wordmark">Saltbush Creek<br>Plumbing</div>
    <div class="divider"></div>
    <div class="services">
      <div class="primary">Domestic &amp; Commercial Plumbing</div>
      <div class="secondary">Tip Truck &amp; Excavator <em>hire</em></div>
    </div>
    <div class="details">
      <div>enquiries@scplumbingco.net.au</div>
      <div>ABN: 47 815 203 966</div>
      <div>PCL: 4187</div>
    </div>
  </section>

  <section class="sheet letterhead" aria-label="Letterhead">
    <div class="wordmark">Saltbush Creek<br>Plumbing</div>
    <div class="tagline">Domestic &amp; Commercial Plumbing <span class="sep">|</span> Tip Truck &amp; Excavator <em>hire</em></div>
    <div class="footer-bar">
      <span>ABN: 47 815 203 966</span>
      <span class="contact">
        <svg class="icon" viewBox="0 0 10 8"><rect x=".5" y=".5" width="9" height="7" fill="none" stroke="#fff"/><path d="M.5 .5 5 4.5 9.5 .5" fill="none" stroke="#fff"/></svg>
        enquiries@scplumbingco.net.au
        <svg class="icon" viewBox="0 0 6 10"><rect x=".5" y=".5" width="5" height="9" rx="1" fill="none" stroke="#fff"/></svg>
        0481 362 740
      </span>
      <span>PCL: 4187</span>
    </div>
  </section>

  <section class="sheet envelope-front" aria-label="Envelope front">
    <div class="wordmark">Saltbush Creek<br>Plumbing</div>
    <div class="top-rule"></div>
    <div class="return-block">
      <div class="services">Domestic &amp; Commercial Plumbing<br>Tip Truck &amp; Excavator <em>hire</em></div>
      <div class="rule"></div>
      <div>enquiries@scplumbingco.net.au &nbsp;0481 362 740</div>
      <div>ABN: 47 815 203 966</div>
      <div>PCL: 4187</div>
    </div>
  </section>

  <section class="sheet envelope-back" aria-label="Envelope back">
    <svg width="414" height="170" viewBox="0 0 414 170">
      <path d="M0 0 H414 V2 C414 22 400 30 380 32 L207 54 L34 32 C14 30 0 22 0 2 Z" fill="var(--brand-navy)"/>
    </svg>
  </section>

</body>
</html>
```